Machine shop needs a brochure designed

Would like a tri-fold professional looking brochure that tells about our business and our capabilities. We are a family-owned business with over 50 years of experience in precision manufacturing. We specialize in close-tolerance tooling and serve a diverse array of industries. Our colors are red, black, white, and gray. The final design should make a great impression and spotlight our capabilities and quality.

Target Market(s)

Manufacturing industries needing tooling

Industry/Entity Type

Machining, grinding, manufacturing

Font styles to use
Serif

Colors
EB3D1F
EC4F4E
F09395
F8D3D4
FCEDEE

Requirements
Must have
• Logo, colors are red, black, white, gray
Nice to have
• Images of CNC process or machining/grinding metal parts.

```html
<!DOCTYPE html>
<html lang="en">
<head>
<meta charset="utf-8">
<title>Hartwell Precision, Inc. – Tri-fold Brochure</title>
<link rel="stylesheet" href="https://fonts.googleapis.com/css2?family=Tinos:wght@400;700&family=Arimo:wght@400;700&display=swap">
<style>
  :root {
    --red: #f20a0a;
    --red-deep: #c8161a;
    --dark-gray: #4a4a4c;
    --mid-gray: #8d9096;
    --light-gray: #e9e9ea;
    --ink: #1d1d1f;
    --white: #ffffff;
    --page-bg: #efefef;
  }
  * { margin: 0; padding: 0; box-sizing: border-box; }
  html, body { width: 898px; height: 1200px; overflow: hidden; }
  body { background: var(--page-bg); font-family: "Arimo", Arial, sans-serif; color: var(--ink); position: relative; }

  .spread { position: absolute; left: 29px; width: 840px; height: 510px; background: var(--white); box-shadow: 0 2px 10px rgba(0,0,0,.18); overflow: hidden; }
  .spread--outside { top: 40px; }
  .spread--inside { top: 630px; }
  .spread__art { position: absolute; inset: 0; }
  .abs { position: absolute; }

  .serif { font-family: "Tinos", "Times New Roman", serif; }
  .body-copy { font-size: 9.3px; line-height: 14.2px; }
  .body-copy p + p { margin-top: 13px; }
  .on-red { color: var(--white); }

  .brand { display: flex; align-items: flex-end; gap: 5px; font-family: "Tinos", "Times New Roman", serif; font-size: 13px; letter-spacing: .3px; color: var(--ink); }
  .brand__mark { width: 9px; height: 9px; background: var(--red); margin-bottom: 4px; }
  .brand--small { font-size: 11px; }
  .brand--small .brand__mark { width: 7px; height: 7px; margin-bottom: 3px; }

  /* outside */
  .qa-title { left: 35px; top: 36px; font-size: 20px; font-weight: 700; line-height: 22px; }
  .qa-badge { left: 34px; top: 100px; }
  .qa-copy { left: 35px; top: 225px; width: 226px; }
  .contact { left: 309px; top: 314px; }
  .contact__title { font-size: 15.5px; font-weight: 700; color: var(--white); margin-bottom: 8px; }
  .contact__line { display: flex; align-items: center; gap: 6px; color: var(--white); font-size: 9px; font-weight: 700; height: 18px; }
  .contact__line svg { flex: none; }
  .contact__fax { margin-left: 10px; display: inline-flex; align-items: center; gap: 3px; }
  .welcome-copy { left: 585px; top: 350px; width: 228px; }
  .footer-web { font-size: 6.5px; font-weight: 700; color: var(--white); }
  .footer-phone { display: flex; align-items: center; gap: 5px; font-size: 9.5px; font-weight: 700; color: var(--white); }

  /* inside */
  .about { left: 37px; top: 22px; width: 232px; }
  .about__title { font-size: 21px; font-weight: 700; color: var(--red); margin-bottom: 4px; }
  .about strong { font-weight: 700; }
  .about__sign { margin-top: 12px; font-size: 9.3px; line-height: 12px; display: flex; gap: 22px; }
  .about__sign b { font-weight: 700; }
  .about__cta { left: 20px; width: 260px; top: 478px; text-align: center; font-size: 9.5px; font-weight: 700; color: var(--red); line-height: 12px; }
  .cap-title { left: 306px; top: 150px; font-size: 38px; font-weight: 700; color: var(--white); }
  .cap-sub { left: 306px; top: 204px; width: 240px; font-size: 9.5px; line-height: 14px; color: var(--white); }
  .cap-head { left: 304px; top: 280px; font-size: 11px; font-weight: 700; }
  .cap-list { list-style: none; font-size: 9.8px; line-height: 12px; }
  .cap-list li { display: flex; gap: 7px; margin-bottom: 7.5px; }
  .cap-list li svg { flex: none; margin-top: 1px; }
  .cap-list--left { left: 314px; top: 306px; width: 230px; }
  .cap-list--right { left: 590px; top: 310px; width: 225px; }
  .inside-footer-web { left: 608px; top: 493px; font-size: 6.5px; font-weight: 700; }
  .inside-footer-phone { left: 760px; top: 490px; font-size: 10px; font-weight: 700; }
</style>
</head>
<body>

<!-- Outside spread -->
<section class="spread spread--outside" aria-label="Brochure outside">
  <svg class="spread__art" width="840" height="510" viewBox="0 0 840 510">
    <defs>
      <linearGradient id="machineTone" x1="0" y1="0" x2="0" y2="1">
        <stop offset="0" stop-color="#ffffff"/>
        <stop offset=".35" stop-color="#c7c9cd"/>
        <stop offset="1" stop-color="#7f848b"/>
      </linearGradient>
    </defs>
    <rect class="photo" x="280" y="0" width="560" height="320" fill="url(#machineTone)" role="img" aria-label="Photo of a CNC lathe turning a steel part"/>
    <polygon fill="#3f3f41" points="455,262 560,198 560,305"/>
    <polygon fill="#4a4a4c" points="720,190 840,210 840,295"/>
    <polygon fill="var(--red)" points="0,195 280,195 560,305 560,510 0,510"/>
    <polygon fill="var(--red)" points="560,198 840,295 840,510 560,510"/>
    <line x1="560" y1="305" x2="560" y2="510" stroke="#d70707" stroke-width="1"/>
  </svg>

  <h2 class="abs serif qa-title">Hartwell Precision<br>Quality Assurance</h2>
  <svg class="abs qa-badge" width="90" height="90" viewBox="0 0 90 90" aria-hidden="true">
    <circle cx="45" cy="45" r="40" fill="none" stroke="var(--dark-gray)" stroke-width="4"/>
    <circle cx="45" cy="45" r="32" fill="none" stroke="var(--dark-gray)" stroke-width="1.5"/>
  </svg>

  <div class="abs body-copy on-red qa-copy">
    <p>Hartwell Precision, Inc. is committed to quality and consistency. We are constantly striving to implement new ways to adhere to a high mark while providing our clients with their orders in as short a time frame as possible. It is not only our goal, but we understand it to be our responsibility to provide our clients with the highest quality products.</p>
    <p>The inspection process at Hartwell Precision, Inc. begins immediately upon receipt of our materials. All materials are inspected to ensure consistency and are re-inspected throughout the entire process, right up to shipping. We inspect 100% of our parts and catalog all of our orders prior to shipment. We have our own written Quality Assurance program that is specific to our operations and available upon request.</p>
  </div>

  <div class="abs contact">
    <h3 class="serif contact__title">Contact Info</h3>
    <div class="contact__line">
      <svg width="11" height="12" viewBox="0 0 10 12"><path d="M5 0a4 4 0 0 0-4 4c0 3 4 8 4 8s4-5 4-8a4 4 0 0 0-4-4zm0 5.6a1.6 1.6 0 1 1 0-3.2 1.6 1.6 0 0 1 0 3.2z" fill="#fff"/></svg>
      1450 Ridgeway Mill Road
    </div>
    <div class="contact__line">
      <svg width="11" height="12" viewBox="0 0 10 12"><path d="M5 0a4 4 0 0 0-4 4c0 3 4 8 4 8s4-5 4-8a4 4 0 0 0-4-4zm0 5.6a1.6 1.6 0 1 1 0-3.2 1.6 1.6 0 0 1 0 3.2z" fill="#fff"/></svg>
      Fairview, TN 37062
    </div>
    <div class="contact__line">
      <svg width="11" height="11" viewBox="0 0 12 12"><circle cx="6" cy="6" r="6" fill="#fff"/><path d="M3.6 3.2l1.3-.4.8 1.7-.8.6c.4.9 1 1.5 1.9 1.9l.6-.8 1.7.8-.4 1.3c-2.6.2-5.3-2.5-5.1-5.1z" fill="var(--red)"/></svg>
      555.014.2210
      <span class="contact__fax">
        <svg width="11" height="10" viewBox="0 0 11 10"><rect x="2.5" y="0" width="6" height="3" fill="#fff"/><rect x="0" y="3" width="11" height="4.5" rx="1" fill="#fff"/><rect x="2.5" y="6" width="6" height="4" fill="#fff" stroke="var(--red)" stroke-width=".8"/></svg>
        555.014.2211
      </span>
    </div>
    <div class="contact__line">
      <svg width="11" height="9" viewBox="0 0 11 8"><rect width="11" height="8" fill="#fff"/><path d="M0 0l5.5 4.5L11 0" fill="none" stroke="var(--red)" stroke-width="1"/></svg>
      info@hartwellprecision.example
    </div>
    <div class="contact__line">
      <svg width="11" height="11" viewBox="0 0 12 12"><circle cx="6" cy="6" r="5.3" fill="none" stroke="#fff" stroke-width="1.2"/><ellipse cx="6" cy="6" rx="2.3" ry="5.3" fill="none" stroke="#fff" stroke-width="1"/><path d="M.7 6h10.6M1.6 3.4h8.8M1.6 8.6h8.8" stroke="#fff" stroke-width="1"/></svg>
      www.hartwellprecision.example
    </div>
  </div>

  <div class="abs brand" style="right:28px; top:22px;"><span class="brand__mark"></span>HARTWELL PRECISION, INC.</div>

  <div class="abs body-copy on-red welcome-copy">
    <p>When your project or process requires precise, high-quality parts or components, look no further than Hartwell. We welcome the opportunity to quote your project, and with 40 years combined experience in precision manufacturing, you can rest assured that jobs placed with us will be done to your satisfaction, &nbsp;every time.</p>
  </div>

  <div class="abs footer-web" style="left:584px; top:484px;">www.hartwellprecision.example</div>
  <div class="abs footer-phone" style="right:30px; top:480px;">
    <svg width="12" height="12" viewBox="0 0 12 12"><circle cx="6" cy="6" r="6" fill="#fff"/><path d="M3.6 3.2l1.3-.4.8 1.7-.8.6c.4.9 1 1.5 1.9 1.9l.6-.8 1.7.8-.4 1.3c-2.6.2-5.3-2.5-5.1-5.1z" fill="var(--red)"/></svg>
    555.014.2210
  </div>
</section>

<!-- Inside spread -->
<section class="spread spread--inside" aria-label="Brochure inside">
  <svg class="spread__art" width="840" height="510" viewBox="0 0 840 510">
    <defs>
      <linearGradient id="aboutTone" x1="0" y1="0" x2="1" y2="0">
        <stop offset="0" stop-color="#e6e7e9"/>
        <stop offset=".6" stop-color="#f7f7f8"/>
        <stop offset="1" stop-color="#ffffff"/>
      </linearGradient>
      <linearGradient id="partsTone" x1="0" y1="0" x2="0" y2="1">
        <stop offset="0" stop-color="#5c6068"/>
        <stop offset=".45" stop-color="#3a3c42"/>
        <stop offset=".8" stop-color="#8a1c22"/>
        <stop offset="1" stop-color="#d0161c"/>
      </linearGradient>
    </defs>
    <rect x="0" y="0" width="280" height="510" fill="url(#aboutTone)"/>
    <rect class="photo" x="280" y="0" width="560" height="262" fill="url(#partsTone)" role="img" aria-label="Photo of machined steel shafts, gears and tooling parts"/>
  </svg>

  <div class="abs about body-copy">
    <h2 class="serif about__title">About us</h2>
    <p><strong>Hartwell Precision, Inc.</strong> is a privately owned company with over fifty years of experience in precision manufacturing. Products manufactured include components for guided defense systems during the early 1990s, machine gun barrels, close tolerance can tooling, conveyor slats and rollers, molds, various production tooling for several national industries, pump housings for the gasoline industry, aviation and automotive manufacturing, and various precision machining and grinding jobs.</p>
    <p>Currently, Hartwell Precision, Inc. is working with a group of physicians to develop and patent various surgical devices for use in Orthopedic and General Vascular surgeries.</p>
    <p>We at Hartwell Precision, Inc. look forward to the opportunity to work with you and quote any projects you might want us to look at. We take a “Quality first” approach to all of our jobs and we have the determination to get the job done according to our clients’ timelines. We are always looking for opportunities to form new alliances and friendships with prospective clients.</p>
    <p style="margin-top:12px;"><b>Best regards,</b></p>
    <div class="about__sign">
      <div><b>Daniel R. Hartwell</b><br>President / Shop Manager</div>
      <div><b>Laura Hartwell</b><br>COO</div>
    </div>
  </div>
  <div class="abs about__cta">Contact us today and let us help you make<br>your product a success!</div>

  <h2 class="abs serif cap-title">Capabilities</h2>
  <p class="abs cap-sub">We at Hartwell offer a wide variety of services to meet your machining and tooling needs.</p>
  <h3 class="abs cap-head">Our capabilities include</h3>

  <ul class="abs cap-list cap-list--left">
    <li><svg width="9" height="9" viewBox="0 0 9 9"><rect width="9" height="9" fill="var(--ink)"/><path d="M2 4.6l1.7 1.7L7 2.8" fill="none" stroke="#fff" stroke-width="1.3"/></svg>Soft cutting</li>
    <li><svg width="9" height="9" viewBox="0 0 9 9"><rect width="9" height="9" fill="var(--ink)"/><path d="M2 4.6l1.7 1.7L7 2.8" fill="none" stroke="#fff" stroke-width="1.3"/></svg>Hard cutting</li>
    <li><svg width="9" height="9" viewBox="0 0 9 9"><rect width="9" height="9" fill="var(--ink)"/><path d="M2 4.6l1.7 1.7L7 2.8" fill="none" stroke="#fff" stroke-width="1.3"/></svg>CNC Machining</li>
    <li><svg width="9" height="9" viewBox="0 0 9 9"><rect width="9" height="9" fill="var(--ink)"/><path d="M2 4.6l1.7 1.7L7 2.8" fill="none" stroke="#fff" stroke-width="1.3"/></svg>CNC Milling</li>
    <li><svg width="9" height="9" viewBox="0 0 9 9"><rect width="9" height="9" fill="var(--ink)"/><path d="M2 4.6l1.7 1.7L7 2.8" fill="none" stroke="#fff" stroke-width="1.3"/></svg><span>Grinding- O.D./ I.D. and Surface/Rotary<br>(Carbide, Steel, etc.)</span></li>
    <li><svg width="9" height="9" viewBox="0 0 9 9"><rect width="9" height="9" fill="var(--ink)"/><path d="M2 4.6l1.7 1.7L7 2.8" fill="none" stroke="#fff" stroke-width="1.3"/></svg>0-2 Micro-finishing</li>
  </ul>

  <ul class="abs cap-list cap-list--right">
    <li><svg width="9" height="9" viewBox="0 0 9 9"><rect width="9" height="9" fill="var(--ink)"/><path d="M2 4.6l1.7 1.7L7 2.8" fill="none" stroke="#fff" stroke-width="1.3"/></svg>Light fabrication</li>
    <li><svg width="9" height="9" viewBox="0 0 9 9"><rect width="9" height="9" fill="var(--ink)"/><path d="M2 4.6l1.7 1.7L7 2.8" fill="none" stroke="#fff" stroke-width="1.3"/></svg>Conveyor assemblies - slats, rollers, etc</li>
    <li><svg width="9" height="9" viewBox="0 0 9 9"><rect width="9" height="9" fill="var(--ink)"/><path d="M2 4.6l1.7 1.7L7 2.8" fill="none" stroke="#fff" stroke-width="1.3"/></svg><span>Can tooling- Trimmer Knives, Knockouts, Punch Bolts, Printer Mandrels, Cut Edges, Blank and Draw Dies, etc</span></li>
    <li><svg width="9" height="9" viewBox="0 0 9 9"><rect width="9" height="9" fill="var(--ink)"/><path d="M2 4.6l1.7 1.7L7 2.8" fill="none" stroke="#fff" stroke-width="1.3"/></svg><span>Wide range of Aerospace and Automotive tooling</span></li>
    <li><svg width="9" height="9" viewBox="0 0 9 9"><rect width="9" height="9" fill="var(--ink)"/><path d="M2 4.6l1.7 1.7L7 2.8" fill="none" stroke="#fff" stroke-width="1.3"/></svg>NAICS 332813, 332721 &amp; 333512</li>
  </ul>

  <div class="abs brand brand--small" style="left:325px; top:486px;"><span class="brand__mark"></span>HARTWELL PRECISION, INC.</div>
  <div class="abs inside-footer-web">www.hartwellprecision.example</div>
  <div class="abs inside-footer-phone">555.014.2210</div>
</section>

</body>
</html>
```